【 概要 】 都内で7年目のイタリアンレストランです。 コロナ渦でテイクアウト営業に勤しんでおります。 今までスタッフが書いたチラシで頑張ってましたが、メニュー改訂もあり是非プロのお力添えを頂きたく募集致しました。 素敵なデザインを楽しみにしております。 【 依頼内容 】 ・サイズ:A4 片面 ・ページ数:1ページ ・素材の用意(画像・文章等):添付ファイル1枚目がメニューです ・デザイン内容:添付ファイル2枚目がイメージです。料理や人物を参考にお願いします 【 デザインイメージ 】 ・ターゲット層:都心在住の30〜50代男女 ・雰囲気:ナチュラルでおしゃれな雰囲気 ・参考デザイン: お店のイメージ(URL参考)添付ファイル2枚目参照 【 契約金額(税抜) 】 2万円 ※契約金額(税込)からシステム利用料を差し引いた金額が、ワーカーさまの受取金額となります その他ご質問等ありましたら、気軽にお問い合わせください。 ご応募をお待ちしております! |
| https://find.kumoriba.co.jp/amp/s/s.shokunavi-ranpo.jp/tokyo/B2401/B240305/24085917/top_amp/%3Fusqp%3Dxr482KZTMBHZBafV9N3q9-vY6RHxBTB%253D | ||
この度は有難うございます。また細かな修正も早急に対応してくださりありがたかったです。お陰で妥協なくイメージしたデザインに仕上がりました。スキルも高く誠意も伝わりとても感謝致します。また機会がございましたら宜しくお願い致します。
この度は皆様素敵なデザインをありがとうございました!皆様の素敵なデザインに感動し感謝の気持ちでいっぱいでした。コロナ渦で皆様も大変な状況だと思いますが、私も頑張ろうという気持ちになりました。心からありがとうございました。

```html
<!DOCTYPE html>
<html lang="ja">
<head>
<meta charset="utf-8">
<title>Trattoria Fiorello テイクアウトメニュー</title>
<link href="https://fonts.googleapis.com/css2?family=M+PLUS+Rounded+1c:wght@400;500;700;800&display=swap" rel="stylesheet">
<style>
:root{
  --green:#3d9a3f;
  --green-dark:#2c7a30;
  --red:#d7352b;
  --orange:#e8842a;
  --ink:#2b2b2b;
  --paper:#ffffff;
  --cream:#fdf5d6;
  --mint:#e9f4e2;
  --pink:#fbe7e3;
  --line:#d8cfa6;
}
*{box-sizing:border-box;margin:0;padding:0}
html,body{width:845px;height:1200px;overflow:hidden;background:var(--paper)}
body{font-family:"M PLUS Rounded 1c",sans-serif;color:var(--ink);position:relative}
.garland{position:absolute;left:0;top:0;width:845px;height:70px;
  background:linear-gradient(180deg,#f3e3a0 0%,#e6efd6 60%,rgba(255,255,255,0) 100%)}
.title{position:absolute;left:0;top:22px;width:845px;text-align:center;color:var(--green);
  font-weight:800;font-size:50px;letter-spacing:1px;line-height:1}
.title small{font-size:26px;font-weight:700;margin-left:6px}
.title-rule{position:absolute;left:300px;top:80px}
.section{position:absolute}
.head{font-weight:800;font-size:24px;display:flex;align-items:center;gap:8px;line-height:1}
.head::before{content:"";width:10px;height:24px;background:var(--ink);display:block}
.head .note{font-size:13px;font-weight:700;color:var(--green-dark)}
.photo{border-radius:4px;margin-top:8px}
.list{margin-top:8px;padding:10px 10px;font-size:14.5px;font-weight:700;line-height:1.75;border-radius:4px}
.list li{list-style:none}
.list .price{white-space:nowrap}
.cream{background:var(--cream)}
.mint{background:var(--mint)}
.tag{position:absolute;font-size:12px;font-weight:700;line-height:1.3;text-align:center}
.badge{position:absolute;border-radius:50%;color:#fff;font-weight:800;display:flex;align-items:center;justify-content:center;text-align:center;line-height:1.25}
.label{color:var(--green-dark);font-size:12px}
.star{color:var(--red)}
.footer{position:absolute;left:20px;top:1085px;width:805px;height:105px}
.shop-photo{position:absolute;left:0;top:0;width:110px;height:105px;border-radius:4px;
  background:linear-gradient(160deg,#3b3a36,#7b6a52 60%,#c8b88f)}
.footer .lead{position:absolute;left:130px;top:2px;font-size:15px;font-weight:700}
.footer .name{position:absolute;left:130px;top:24px;font-size:22px;font-weight:800;color:var(--green-dark)}
.footer .tel{position:absolute;left:130px;top:48px;font-size:40px;font-weight:800;color:var(--red);letter-spacing:1px;line-height:1;display:flex;align-items:center;gap:8px}
.footer .addr{position:absolute;left:130px;top:90px;font-size:13px;font-weight:500}
</style>
</head>
<body>

<div class="garland" role="img" aria-label="色とりどりの三角旗のガーランド"></div>
<h1 class="title">TAKEOUT<small>できます</small></h1>
<svg class="title-rule" width="245" height="14" viewBox="0 0 245 14">
  <path d="M2 8 Q20 1 40 8 T80 8 T120 8 T160 8 T200 8 T243 8" fill="none" stroke="#3d9a3f" stroke-width="3" stroke-linecap="round"/>
</svg>

<!-- ANTIPASTO -->
<section class="section" style="left:20px;top:108px;width:262px">
  <h2 class="head">ANTIPASTO</h2>
  <div class="photo" style="height:185px;background:linear-gradient(150deg,#e8d9b6,#c99a5a 55%,#f3ead4)" role="img" aria-label="ゴルゴンゾーラのキッシュの写真"></div>
  <p class="tag" style="left:96px;top:150px;color:var(--red)">大人気! 定番の<br>手作りキッシュ</p>
  <ul class="list cream">
    <li>ゴルゴンゾーラのキッシュ</li>
    <li>（2ピース）・・・<span class="price">600円</span></li>
    <li>アンチョビポテト・・・<span class="price">500円</span></li>
    <li>ピクルス＆オリーブ・・・<span class="price">500円</span></li>
    <li>合鴨のロースト・・・<span class="price">900円</span></li>
    <li>いぶりこのトマト煮・・・<span class="price">950円</span></li>
    <li>ローストビーフ・・・<span class="price">1200円</span></li>
    <li>ローストポーク・・・<span class="price">900円</span></li>
  </ul>
</section>

<!-- PASTA -->
<section class="section" style="left:292px;top:108px;width:262px">
  <h2 class="head">PASTA</h2>
  <div class="photo" style="height:185px;background:linear-gradient(140deg,#d9d3c4,#b9a27a 50%,#8c8474)" role="img" aria-label="はまぐりのボンゴレビアンコの写真"></div>
  <p class="tag" style="left:20px;top:42px;background:#f6e04c;padding:2px 8px;border-radius:10px;color:var(--red)">パスタ専門No.1</p>
  <p class="tag" style="left:150px;top:150px;color:var(--green-dark)">貝のだしが溢れた<br>絶品ボンゴレ</p>
  <ul class="list cream" style="font-size:14px">
    <li>はまぐりと大葉あさりの</li>
    <li>ボンゴレビアンコ・・・<span class="price">1500円</span></li>
    <li>わたりがにの</li>
    <li>トマトクリーム・・・<span class="price">1500円</span></li>
    <li>にんにくとアンチョビの</li>
    <li>ペペロンチーノ・・・<span class="price">900円</span></li>
    <li>ゴルゴンゾーラのペンネ・・<span class="price">1300円</span></li>
    <li>アラビアータのペンネ・・<span class="price">1200円</span></li>
    <li style="font-size:11px;color:#666">※麺は生でもお作りします</li>
  </ul>
</section>

<!-- PIZZA -->
<section class="section" style="left:564px;top:108px;width:262px">
  <h2 class="head">PIZZA</h2>
  <div class="photo" style="height:120px;background:linear-gradient(135deg,#e9c27a,#c9552d 55%,#f2e4c1)" role="img" aria-label="マルゲリータピザの写真"></div>
  <div class="badge" style="left:150px;top:-6px;width:112px;height:74px;border-radius:40px;background:var(--green);font-size:11.5px">シンプルが人気！<br>本場のピザ職人が<br>作る一品！</div>
  <ul class="list" style="font-size:14.5px">
    <li>マルゲリータ・・・<span class="price">1500円</span></li>
    <li class="label">4種のチーズとハチミツの相性抜群</li>
    <li><span class="star">●</span> クワトロフォルマッジョ・・<span class="price">1700円</span></li>
    <li class="label">明太子とクリームが絡む和風のピザ</li>
    <li><span class="star">●</span> 博多明太子のクリームピザ・<span class="price">1600円</span></li>
    <li class="label">自家製ソーセージとキノコの香り</li>
    <li><span class="star">●</span> ザ・サルシッチャ・・・<span class="price">1600円</span></li>
  </ul>
  <svg style="position:absolute;left:200px;top:150px" width="50" height="70" viewBox="0 0 50 70" aria-hidden="true">
    <path d="M12 4v22M18 4v22M24 4v22M12 26h12M18 26v40" stroke="#bbb" stroke-width="3" fill="none" stroke-linecap="round"/>
    <path d="M38 4c8 6 8 22 0 24v38" stroke="#bbb" stroke-width="3" fill="none" stroke-linecap="round"/>
  </svg>
</section>

<!-- SPECIALITA -->
<section class="section" style="left:20px;top:592px;width:390px">
  <h2 class="head">SPECIALITA</h2>
  <div class="photo" style="position:absolute;left:0;top:32px;width:178px;height:170px;margin:0;background:linear-gradient(150deg,#f1e6c4,#d8a25a 55%,#a6c27a)" role="img" aria-label="魚介の蒸し焼きアヒージョの写真"></div>
  <div class="photo" style="position:absolute;left:192px;top:32px;width:198px;height:170px;margin:0;background:linear-gradient(150deg,#e9dcc0,#b88d55 55%,#e3d2ab)" role="img" aria-label="エスカルゴバター焼きの写真"></div>
  <p class="tag" style="left:-4px;top:24px;background:var(--red);color:#fff;padding:3px 8px;border-radius:3px">オススメ!</p>
  <p class="tag" style="left:290px;top:72px;color:#fff">じっくりと旨みを<br>閉じ込めた<br>エスカルゴバター</p>
  <ul class="list" style="position:absolute;left:0;top:208px;width:178px;padding:0;font-size:14px">
    <li>魚介の蒸し焼き</li>
    <li>アヒージョ</li>
    <li>スープ仕立て・・<span class="price">900円</span></li>
  </ul>
  <ul class="list" style="position:absolute;left:192px;top:208px;width:200px;padding:0;font-size:14px">
    <li>つぶ貝と小海老の</li>
    <li>エスカルゴバター・・<span class="price">900円</span></li>
  </ul>
  <div class="photo" style="position:absolute;left:0;top:300px;width:110px;height:170px;margin:0;background:linear-gradient(160deg,#f2e2b4,#d08a3c 60%,#9c5a2b)" role="img" aria-label="ラザニアとクリームコロッケの写真"></div>
  <div class="badge" style="left:-6px;top:290px;width:70px;height:70px;background:var(--orange);font-size:12px">1人前<br>ボリューム<br>満点!</div>
  <ul class="list cream" style="position:absolute;left:120px;top:310px;width:210px;font-size:14px">
    <li>ラザニア・・・・<span class="price">1000円</span></li>
    <li>天使の海老の</li>
    <li>クリームコロッケ・・<span class="price">700円</span></li>
    <li>バケット2ピース・・<span class="price">300円</span></li>
  </ul>
</section>

<!-- INSALATA -->
<section class="section" style="left:425px;top:592px;width:200px">
  <h2 class="head">INSALATA <span class="note">3〜4名様</span></h2>
  <div class="photo" style="height:125px;background:linear-gradient(150deg,#cfe3a8,#7fae4a 55%,#e6e1c7)" role="img" aria-label="シーザーサラダの写真"></div>
  <p class="tag" style="left:40px;top:40px;background:#fff;padding:3px 6px;border-radius:10px;color:var(--red);font-size:11px">アンチョビできかせた<br>ドレッシングが人気!</p>
  <div role="img" aria-label="ワインボトルのイラスト" style="position:absolute;left:150px;top:160px;width:38px;height:70px;border-radius:8px;background:linear-gradient(180deg,#c33 0%,#7d1b1b 100%)"></div>
  <ul class="list mint" style="font-size:13.5px;margin-top:90px">
    <li>FIORELLOの</li>
    <li>シーザーサラダ・・<span class="price">1000円</span></li>
    <li>生ハムの</li>
    <li>グリーンサラダ・・<span class="price">1000円</span></li>
    <li>イタリアンだけど</li>
    <li>フレンチサラダ・・<span class="price">1000円</span></li>
    <li>フレンチサラダ・・<span class="price">450円</span></li>
  </ul>
</section>

<!-- DOLCE -->
<section class="section" style="left:640px;top:592px;width:186px">
  <h2 class="head">DOLCE</h2>
  <div class="photo" style="height:170px;background:linear-gradient(150deg,#f0e4cf,#6b4a32 55%,#d9c3a2)" role="img" aria-label="ティラミスの写真"></div>
  <p class="tag" style="left:6px;top:160px;color:var(--green-dark);font-size:11px">自家製マスカルポーネ<br>のティラミス</p>
  <p style="font-size:15px;font-weight:700;margin-top:6px">ティラミス・・・<span class="price">500円</span></p>
  <div class="photo" style="height:170px;margin-top:14px;background:linear-gradient(150deg,#f6e8ee,#4a2c22 55%,#c6485a)" role="img" aria-label="ガトーショコラの写真"></div>
  <p class="tag" style="left:96px;top:300px;color:var(--red);font-size:11px">濃厚な<br>ガトーショコラ</p>
  <p style="font-size:15px;font-weight:700;margin-top:6px">ガトーショコラ・・<span class="price">500円</span></p>
</section>

<!-- FOOTER -->
<footer class="footer">
  <div class="shop-photo" role="img" aria-label="店舗外観の写真"></div>
  <p class="lead">事前予約お待ちしております。</p>
  <p class="name">Trattoria Fiorello</p>
  <p class="tel">
    <svg width="32" height="32" viewBox="0 0 24 24" aria-hidden="true"><path fill="#d7352b" d="M6.6 10.8a15.1 15.1 0 0 0 6.6 6.6l2.2-2.2a1 1 0 0 1 1-.25 11.4 11.4 0 0 0 3.6.57 1 1 0 0 1 1 1V20a1 1 0 0 1-1 1A17 17 0 0 1 3 4a1 1 0 0 1 1-1h3.5a1 1 0 0 1 1 1c0 1.25.2 2.45.57 3.57a1 1 0 0 1-.25 1z"/></svg>
    03-5550-1842
  </p>
  <p class="addr">〒104-0000 東京都中央区みどり町 2-8-5 みどりビル 1F</p>
</footer>

</body>
</html>
```